Business Card Design

I am a criminologist running a research and consultancy business on my own (RLConsultants)
I specialise in looking at fraud and other white-collar crimes. Also governance issues..
I would like a professional business card that would be appropriate both in the academic and business sector as I straddle both sectors. Normal shape - not square.
I am interested in seeing border Word Cloud type projects - black on white or white on black..
Example key words would be fraud, research, qualitative, interviews, quantitative, white-collar, reports, government, surveys, sample, governance, assurance, crime, offenders, prison etc (I can provide a full list if this is the option I go for). I also like Word Cloud borders as attached.
I am also interested in seeing other style business cards. Preferably one colour, plus black and white.
In particular I like black backgrounds with coloured words etc - colours like lime green are good.
I also like blues - especially teal if a traditional white background is chosen.
I don't have a logo - unless anyone can think of anything that's particularly appropriate.
Graphics can be used but they would be simple and stylish (dots, squares, lines, curves etc)
I would like the design to translate simply for a header for a website or blog.
My current website is www.penmarrow-dale.example but is out of date in terms of what I do and design.
I have attached a number of things that have caught my eye and inspired me.
I have asked for a one-sided business card in the first instance - however if someone comes up with a good cloud design that might go on one side, I would consider a two-sided one.
Design can be landscape or portrait.
Kind Regards
Liz
Industry/Entity Type
Landscape
Contact Information for Business Card
RLConsultants
Dr Hilary Penmarrow-Dale, MSc, BSc, **
42 Fernby Close
Holmbrook, Wealdshire
QX27 4PL
+44(0)1632 960418
+44(0)7700 900582
www.penmarrow-dale.example
hilary@penmarrow-dale.example

```html
<!DOCTYPE html>
<html lang="en">
<head>
<meta charset="utf-8">
<title>RLConsultants – Business Card</title>
<link rel="stylesheet" href="https://fonts.googleapis.com/css2?family=Arimo:wght@400;500&display=swap">
<style>
  :root {
    --page-bg: #eef2f6;
    --card-face: #e4e7e9;
    --card-back: #c9cfd6;
    --ink: #2b2d2f;
    --ink-soft: #3c3f42;
    --tab-face: #f4f5f5;
    --tab-edge: #c2c6ca;
    --hole: #9ea3a8;
    --dial: #f7f8f9;
    --dial-edge: #d3d7db;
  }
  html, body {
    margin: 0;
    width: 1200px;
    height: 920px;
    overflow: hidden;
    background: var(--page-bg);
    font-family: "Arimo", Arial, sans-serif;
    color: var(--ink);
  }
  .stage {
    position: relative;
    width: 1200px;
    height: 920px;
  }
  .card-wrap {
    position: absolute;
    left: 330px;
    width: 540px;
    height: 340px;
  }
  .card-wrap.front { top: 60px; }
  .card-wrap.back  { top: 500px; }

  .dial-row {
    position: absolute;
    left: 0;
    bottom: -22px;
    width: 540px;
    height: 40px;
    z-index: 0;
  }
  .card {
    position: relative;
    z-index: 1;
    width: 540px;
    height: 340px;
    box-sizing: border-box;
    border-radius: 3px;
    box-shadow: 0 10px 24px rgba(60, 80, 100, 0.18);
  }
  .card.front { background: var(--card-face); }
  .card.back  { background: linear-gradient(160deg, var(--card-back), #dfe3e7); }

  .holder-name {
    position: absolute;
    top: 92px;
    left: 0;
    width: 100%;
    text-align: center;
    font-size: 30px;
    font-weight: 400;
    letter-spacing: 0.2px;
    margin: 0;
  }
  .holder-company {
    position: absolute;
    top: 136px;
    left: 0;
    width: 100%;
    text-align: center;
    font-size: 21px;
    color: var(--ink-soft);
    margin: 0;
  }

  .brand {
    position: absolute;
    top: 34px;
    left: 38px;
    margin: 0;
    font-size: 33px;
    font-weight: 500;
  }
  .details {
    position: absolute;
    top: 96px;
    left: 38px;
    font-size: 15px;
    line-height: 20px;
    color: var(--ink-soft);
  }
  .details p { margin: 0; }
  .details .gap { margin-top: 12px; }

  .dial-tabs {
    position: absolute;
    left: 40px;
    right: 40px;
    bottom: 34px;
    display: flex;
    justify-content: space-between;
  }
  .dial-tab {
    display: flex;
    flex-direction: column;
    align-items: center;
    width: 86px;
  }
  .dial-number {
    width: 86px;
    height: 34px;
    line-height: 34px;
    text-align: center;
    font-size: 18px;
    background: var(--tab-face);
    border: 1px solid var(--tab-edge);
    border-radius: 4px;
    box-shadow: inset 0 -3px 4px rgba(0,0,0,0.08);
  }
  .dial-hole {
    margin-top: 8px;
    width: 13px;
    height: 13px;
    border-radius: 50%;
    background: var(--hole);
    box-shadow: inset 0 2px 2px rgba(0,0,0,0.35);
  }
</style>
</head>
<body>
<main class="stage">

  <section class="card-wrap front">
    <svg class="dial-row" viewBox="0 0 540 40" aria-hidden="true">
      <g fill="var(--dial)" stroke="var(--dial-edge)" stroke-width="2" stroke-dasharray="3 2">
        <circle cx="83" cy="6" r="30"/>
        <circle cx="204" cy="6" r="30"/>
        <circle cx="336" cy="6" r="30"/>
        <circle cx="457" cy="6" r="30"/>
      </g>
    </svg>
    <div class="card front">
      <h1 class="holder-name">Dr Hilary Penmarrow-Dale</h1>
      <p class="holder-company">RLConsultants</p>
      <div class="dial-tabs">
        <div class="dial-tab"><span class="dial-number">+44(0)</span><span class="dial-hole"></span></div>
        <div class="dial-tab"><span class="dial-number">1632</span><span class="dial-hole"></span></div>
        <div class="dial-tab"><span class="dial-number">960</span><span class="dial-hole"></span></div>
        <div class="dial-tab"><span class="dial-number">418</span><span class="dial-hole"></span></div>
      </div>
    </div>
  </section>

  <section class="card-wrap back">
    <svg class="dial-row" viewBox="0 0 540 40" aria-hidden="true">
      <g fill="var(--dial)" stroke="var(--dial-edge)" stroke-width="2" stroke-dasharray="3 2">
        <circle cx="83" cy="6" r="30"/>
        <circle cx="204" cy="6" r="30"/>
        <circle cx="336" cy="6" r="30"/>
        <circle cx="457" cy="6" r="30"/>
      </g>
    </svg>
    <div class="card back">
      <h2 class="brand">RLConsultants</h2>
      <div class="details">
        <p>MSc, BSc, ** 42 Fernby Close Holmbrook</p>
        <p>Wealdshire QX27 4PL</p>
        <p class="gap">hilary@penmarrow-dale.example</p>
        <p>penmarrow-dale.example</p>
      </div>
      <div class="dial-tabs">
        <div class="dial-tab"><span class="dial-number">+44(0)</span><span class="dial-hole"></span></div>
        <div class="dial-tab"><span class="dial-number">7700</span><span class="dial-hole"></span></div>
        <div class="dial-tab"><span class="dial-number">900</span><span class="dial-hole"></span></div>
        <div class="dial-tab"><span class="dial-number">582</span><span class="dial-hole"></span></div>
      </div>
    </div>
  </section>

</main>
</body>
</html>
```